Kestrel Ledger company needs ad for trade publication

Kestrel Ledgers provides sales, content, production, technology, and promotion products and services to radio stations to help increase sales and solutions to improve operations and reduce costs. We are looking for a creative ad (sizes 720x250, 300x250, 728x180) with a halloween theme. An angle could be "Nothing Scarier than starting the new year in the RED" which in business terms is a net operating loss. OR "Take a bite out of your 2024 budget". Kestrel Ledgers CAN HELP!
We want to highlight on the ad 3 key benefits that Kestrel Ledgers can help (1) "Improve your NTR" (2) "Improve your cash flow" (3) "Improve your technology and operations"
Targeting radio stations during their 2024 budgeting process

```html
<!DOCTYPE html>
<html lang="en">
<head>
<meta charset="utf-8">
<title>Kestrel Ledgers – Halloween Budget Ads</title>
<link rel="stylesheet" href="https://fonts.googleapis.com/css2?family=Montserrat:wght@900&family=Poppins:wght@500;600;700;800&display=swap">
<style>
  :root {
    --board: #393735;
    --sky-blue: #0a9af0;
    --pumpkin: #ff4b00;
    --navy: #2b3990;
    --ice: #d6ecfc;
    --wave-light: #8fcdfb;
    --wave-deep: #2f9cf6;
    --white: #ffffff;
  }
  * { margin: 0; padding: 0; box-sizing: border-box; }
  html, body { width: 1062px; height: 1200px; overflow: hidden; }
  body { background: var(--board); font-family: "Poppins", sans-serif; position: relative; }

  .ad {
    position: absolute;
    overflow: hidden;
    background: linear-gradient(180deg, var(--white) 35%, var(--ice) 100%);
    box-shadow: 4px 6px 10px rgba(0,0,0,.55);
  }
  .ad > * { position: absolute; }
  .ad--square { left: 327px; top: 58px; width: 407px; height: 338px; }
  .ad--wide   { left: 42px;  top: 464px; width: 977px; height: 338px; }
  .ad--slim   { left: 37px;  top: 860px; width: 987px; height: 244px; }

  .wave { left: 0; top: 0; width: 100%; height: 100%; }

  .headline { font-weight: 800; line-height: 1; letter-spacing: -1px; white-space: nowrap; }
  .headline--blue { color: var(--sky-blue); }
  .headline--orange { color: var(--pumpkin); }
  .headline--navy { color: var(--navy); }
  .spooky { font-family: "Montserrat", sans-serif; font-weight: 900; line-height: 1; white-space: nowrap; }

  .help-band {
    left: 0;
    background: var(--navy);
    color: var(--white);
    font-weight: 800;
    line-height: 1;
    letter-spacing: -1px;
    white-space: nowrap;
    display: flex;
    align-items: center;
  }

  .improve { color: var(--pumpkin); font-weight: 700; line-height: 1; white-space: nowrap; }
  .rule { height: 1.5px; background: var(--navy); }

  .benefit { display: flex; align-items: center; color: var(--navy); font-weight: 600; white-space: nowrap; line-height: 1; }
  .benefit svg { flex: none; }

  .brand { color: var(--navy); font-weight: 700; line-height: .95; display: flex; align-items: center; gap: 8px; }
  .brand-dot { border-radius: 50%; background: var(--sky-blue); flex: none; }

  .witch-art {
    background: radial-gradient(ellipse at 55% 50%, #2b3990 0%, #2b3990 45%, rgba(43,57,144,0) 72%);
    opacity: .9;
  }
</style>
</head>
<body>

<svg width="0" height="0" style="position:absolute">
  <defs>
    <symbol id="icon-check" viewBox="0 0 40 40">
      <circle cx="20" cy="20" r="17.5" fill="none" stroke="#2b3990" stroke-width="2"/>
      <path d="M11 20 l6 6 l12 -13" fill="none" stroke="#0a9af0" stroke-width="4" stroke-linecap="round" stroke-linejoin="round"/>
    </symbol>
    <symbol id="icon-cash" viewBox="0 0 40 40">
      <path d="M8 26 A14 14 0 0 1 26 7" fill="none" stroke="#2b3990" stroke-width="2"/>
      <path d="M32 14 A14 14 0 0 1 14 33" fill="none" stroke="#2b3990" stroke-width="2"/>
      <path d="M23 4 l4 3 l-4 3" fill="none" stroke="#2b3990" stroke-width="2"/>
      <path d="M17 30 l-4 3 l4 3" fill="none" stroke="#2b3990" stroke-width="2"/>
      <text x="20" y="27" text-anchor="middle" font-family="Poppins, sans-serif" font-weight="700" font-size="20" fill="#0a9af0">$</text>
    </symbol>
    <symbol id="icon-gear" viewBox="0 0 40 40">
      <path d="M8 26 A14 14 0 0 1 26 7" fill="none" stroke="#2b3990" stroke-width="2"/>
      <path d="M32 14 A14 14 0 0 1 14 33" fill="none" stroke="#2b3990" stroke-width="2"/>
      <path d="M23 4 l4 3 l-4 3" fill="none" stroke="#2b3990" stroke-width="2"/>
      <path d="M17 30 l-4 3 l4 3" fill="none" stroke="#2b3990" stroke-width="2"/>
      <circle cx="20" cy="20" r="8" fill="none" stroke="#0a9af0" stroke-width="4" stroke-dasharray="3 2"/>
      <circle cx="20" cy="20" r="5" fill="#ffffff" stroke="#0a9af0" stroke-width="1.5"/>
      <path d="M17.5 20 l2 2 l3.5 -4" fill="none" stroke="#0a9af0" stroke-width="1.5"/>
    </symbol>
  </defs>
</svg>

<!-- Square ad -->
<section class="ad ad--square">
  <svg class="wave" viewBox="0 0 407 338" preserveAspectRatio="none" aria-hidden="true">
    <path d="M193,0 C215,45 300,30 335,62 C365,92 340,115 372,135 C395,150 402,160 407,170 L407,0 Z" fill="#cfe8fd"/>
    <path d="M215,0 C240,35 310,25 345,55 C375,85 355,110 385,128 C400,140 405,150 407,155 L407,0 Z" fill="var(--wave-light)"/>
    <path d="M300,0 C320,20 360,25 380,50 C395,70 400,90 407,100 L407,0 Z" fill="var(--wave-deep)" opacity=".55"/>
  </svg>
  <div class="witch-art" role="img" aria-label="Silhouette of a witch with a cat flying on a broomstick" style="left:258px;top:12px;width:135px;height:115px;"></div>

  <div class="headline headline--blue" style="left:18px;top:24px;font-size:52px;">TAKE A</div>
  <div class="headline headline--orange" style="left:18px;top:83px;font-size:52px;">BITE OUT</div>
  <div class="headline headline--navy" style="left:18px;top:130px;font-size:25px;letter-spacing:-.5px;">OF YOUR 2024 BUDGET</div>

  <div class="help-band" style="top:169px;width:407px;height:40px;padding-left:18px;font-size:25px;letter-spacing:-.5px;">KESTREL LEDGERS CAN HELP!</div>

  <div class="improve" style="left:18px;top:226px;font-size:20px;">IMPROVE YOUR</div>
  <div class="benefit" style="left:17px;top:262px;font-size:13px;gap:8px;">
    <svg width="25" height="25"><use href="#icon-check"/></svg>NTR
  </div>
  <div class="benefit" style="left:106px;top:260px;font-size:13px;gap:8px;">
    <svg width="25" height="25"><use href="#icon-cash"/></svg>Cash Flow
  </div>
  <div class="benefit" style="left:16px;top:294px;font-size:13px;gap:7px;">
    <svg width="25" height="25"><use href="#icon-gear"/></svg>Technology &amp; Operations
  </div>

  <div class="brand" style="left:236px;top:250px;font-size:26px;">
    <span class="brand-dot" style="width:12px;height:12px;"></span>
    <span>Kestrel<br>Ledgers</span>
  </div>
</section>

<!-- Wide ad -->
<section class="ad ad--wide">
  <svg class="wave" viewBox="0 0 977 338" preserveAspectRatio="none" aria-hidden="true">
    <path d="M633,338 C660,262 720,245 790,255 C840,262 850,200 880,170 C910,140 935,160 952,135 C970,110 965,100 977,88 L977,338 Z" fill="#bfe1fd"/>
    <path d="M660,338 C690,280 740,268 800,272 C850,275 870,215 900,185 C930,158 950,170 965,150 C975,135 975,125 977,120 L977,338 Z" fill="var(--wave-light)"/>
    <path d="M760,338 C800,310 860,300 900,260 C935,225 950,200 977,190 L977,338 Z" fill="var(--wave-deep)" opacity=".7"/>
  </svg>
  <div class="witch-art" role="img" aria-label="Silhouette of a witch with a cat flying on a broomstick" style="left:712px;top:133px;width:235px;height:205px;"></div>

  <div class="headline" style="left:32px;top:36px;font-size:75px;letter-spacing:-2px;">
    <span class="headline--blue">TAKE A</span> <span class="headline--orange">BITE OUT</span>
  </div>
  <div class="headline headline--navy" style="left:33px;top:110px;font-size:44px;">OF YOUR 2024 BUDGET</div>

  <div class="help-band" style="top:176px;width:635px;height:46px;padding-left:32px;font-size:39px;">KESTREL LEDGERS CAN HELP!</div>

  <div class="rule" style="left:37px;top:250px;width:174px;"></div>
  <div class="improve" style="left:220px;top:237px;font-size:26px;">IMPROVE YOUR</div>
  <div class="rule" style="left:423px;top:250px;width:181px;"></div>

  <div class="benefit" style="left:33px;top:286px;font-size:21px;gap:9px;">
    <svg width="32" height="32"><use href="#icon-check"/></svg>NTR
  </div>
  <div class="benefit" style="left:135px;top:286px;font-size:21px;gap:12px;">
    <svg width="32" height="32"><use href="#icon-cash"/></svg>Cash Flow
  </div>
  <div class="benefit" style="left:307px;top:286px;font-size:21px;gap:14px;">
    <svg width="32" height="32"><use href="#icon-gear"/></svg>Technology &amp; Operations
  </div>

  <div class="brand" style="left:729px;top:28px;font-size:42px;gap:12px;">
    <span class="brand-dot" style="width:18px;height:18px;"></span>
    <span>Kestrel<br>Ledgers</span>
  </div>
</section>

<!-- Slim ad -->
<section class="ad ad--slim">
  <svg class="wave" viewBox="0 0 987 244" preserveAspectRatio="none" aria-hidden="true">
    <path d="M682,244 C710,180 770,170 820,175 C860,150 870,90 905,70 C940,48 962,58 987,18 L987,244 Z" fill="#bfe1fd"/>
    <path d="M705,244 C735,195 790,188 835,190 C875,168 890,110 920,92 C950,75 970,80 987,55 L987,244 Z" fill="var(--wave-light)"/>
    <path d="M800,244 C840,225 890,215 930,180 C960,155 970,135 987,125 L987,244 Z" fill="var(--wave-deep)" opacity=".7"/>
  </svg>
  <div class="witch-art" role="img" aria-label="Silhouette of a witch with a cat flying on a broomstick" style="left:755px;top:45px;width:225px;height:195px;"></div>

  <div class="spooky" style="left:31px;top:27px;font-size:39px;letter-spacing:4px;">
    <span class="headline--blue">NOTHING</span> <span class="headline--orange">SCARIER THAN</span>
  </div>
  <div class="spooky headline--navy" style="left:31px;top:71px;font-size:26px;letter-spacing:3.3px;">STARTING THE NEW YEAR IN THE RED</div>

  <div class="help-band" style="top:109px;width:634px;height:46px;padding-left:30px;font-size:39px;">KESTREL LEDGERS CAN HELP!</div>

  <div class="improve" style="left:31px;top:165px;font-size:20px;">IMPROVE YOUR</div>
  <div class="rule" style="left:193px;top:175px;width:426px;"></div>

  <div class="benefit" style="left:29px;top:195px;font-size:21px;gap:9px;">
    <svg width="32" height="32"><use href="#icon-check"/></svg>NTR
  </div>
  <div class="benefit" style="left:131px;top:195px;font-size:21px;gap:12px;">
    <svg width="32" height="32"><use href="#icon-cash"/></svg>Cash Flow
  </div>
  <div class="benefit" style="left:303px;top:195px;font-size:21px;gap:14px;">
    <svg width="32" height="32"><use href="#icon-gear"/></svg>Technology &amp; Operations
  </div>

  <div class="brand" style="left:676px;top:22px;font-size:30px;gap:9px;">
    <span class="brand-dot" style="width:14px;height:14px;"></span>
    <span>Kestrel<br>Ledgers</span>
  </div>
</section>

</body>
</html>
```